Business Card Stationary and shirt design for Electrical Company
Corbishaw Electric LLC
Business Card Stationary and shirt design for Electrical Company - Construction
Creative Brief
Bright & Fun-filled
Owner
614 Linwood Avenue Jersey City, NJ 07305
1-855-48AMPRO
corbishawelectricllc@brivanmail.com
www.corbishawelectric-example.com
Highly rated : TradeRankr, Zorvik, NestGauge residential, commercial, industrial
Name of Business Logo web adress simple yet eye catching back (ill leave it up to the designer)

```html
<!DOCTYPE html>
<html lang="en">
<head>
<meta charset="utf-8">
<title>Corbishaw Electric LLC – Stationery Set</title>
<link href="https://fonts.googleapis.com/css2?family=Open+Sans:wght@400;700;800&display=swap" rel="stylesheet">
<style>
  :root{
    --navy:#1f2b3a;
    --green:#8cc63f;
    --paper:#ffffff;
    --ink:#3a3f45;
    --bg-top:#d8d8d8;
    --bg-bottom:#a9a9a9;
  }
  html,body{margin:0;padding:0;overflow:hidden;}
  body{width:1200px;height:206px;font-family:"Open Sans",sans-serif;}
  .board{position:relative;width:1200px;height:206px;overflow:hidden;
    background:linear-gradient(180deg,var(--bg-top),var(--bg-bottom));}
  .piece{position:absolute;box-shadow:0 2px 4px rgba(0,0,0,.35);box-sizing:border-box;}
  .brand{display:flex;align-items:center;gap:4px;font-weight:800;color:var(--green);line-height:1;white-space:nowrap;}
  .brand .dot{width:8px;height:8px;border-radius:50%;background:var(--green);flex:none;}
  .brand.light{color:var(--paper);} .brand.light .dot{background:var(--paper);}
  .tiny{font-size:3.4px;line-height:1.35;color:var(--ink);white-space:nowrap;}

  /* business cards */
  .card-front{left:12px;top:80px;width:170px;height:46px;background:var(--navy);padding:10px 12px;}
  .card-front .brand{font-size:10.5px;}
  .card-front .tag{font-size:4.5px;color:var(--green);margin-top:4px;letter-spacing:.3px;}
  .card-back{left:12px;top:134px;width:170px;height:34px;background:var(--green);padding:6px 10px;}
  .card-back .brand{font-size:8px;margin-bottom:3px;}
  .card-back .tiny{color:var(--navy);}

  /* letterheads */
  .letter{top:58px;width:112px;height:134px;background:var(--paper);padding:7px 8px;}
  .letter .brand{font-size:6.5px;}
  .letter .body{margin-top:30px;}
  .letter .foot{position:absolute;left:0;right:0;bottom:0;height:6px;background:var(--navy);border-top:2px solid var(--green);}
  .letter.one{left:204px;} .letter.two{left:326px;}

  /* small cards */
  .note{left:450px;width:120px;height:22px;background:var(--paper);padding:4px 6px;}
  .note .brand{font-size:6px;margin-bottom:2px;}
  .note.a{top:78px;} .note.b{top:106px;} .note.c{top:134px;background:var(--navy);}
  .note.c .tiny{color:var(--green);}

  /* envelope */
  .envelope{left:582px;top:82px;width:120px;height:58px;background:var(--paper);overflow:hidden;}
  .envelope svg{position:absolute;left:0;top:0;}
  .envelope .brand{position:absolute;left:0;right:0;top:38px;justify-content:center;font-size:6.5px;}
  .envelope-back{left:582px;top:146px;width:120px;height:22px;background:var(--paper);padding:4px 6px;}
  .envelope-back .brand{font-size:6px;margin-bottom:2px;}

  /* shirt prints (flat) */
  .shirt{width:54px;height:56px;display:flex;flex-direction:column;align-items:center;justify-content:center;gap:3px;background:var(--paper);}
  .shirt .brand{font-size:4.6px;gap:2px;}
  .shirt .brand .dot{width:5px;height:5px;}
  .shirt .tiny{font-size:3px;}
  .shirt.navy{background:var(--navy);}
  .shirt.navy .tiny{color:var(--green);}
  .s1{left:714px;top:76px;} .s2{left:772px;top:76px;}
  .s3{left:714px;top:138px;} .s4{left:772px;top:138px;}

  /* vehicle wrap panels (flat) */
  .wrap{width:174px;height:62px;background:var(--paper);overflow:hidden;padding:10px 10px;}
  .wrap .brand{font-size:9px;}
  .wrap .tiny{font-size:4px;margin-top:4px;}
  .wrap .band{position:absolute;left:0;right:0;bottom:0;height:16px;background:var(--navy);border-top:3px solid var(--green);
    display:flex;align-items:center;justify-content:flex-end;padding-right:8px;box-sizing:border-box;}
  .wrap .band span{font-size:5px;font-weight:700;color:var(--paper);white-space:nowrap;}
  .w1{left:836px;top:60px;} .w2{left:1016px;top:60px;}
  .w3{left:836px;top:128px;} .w4{left:1016px;top:128px;}
</style>
</head>
<body>
<main class="board">

  <section class="piece card-front">
    <div class="brand"><span class="dot"></span>Corbishaw Electric LLC</div>
    <div class="tag">RESIDENTIAL · COMMERCIAL · INDUSTRIAL</div>
  </section>

  <section class="piece card-back">
    <div class="brand light"><span class="dot"></span>Owner</div>
    <div class="tiny">614 Linwood Avenue Jersey City, NJ 07305 · 1-855-48AMPRO<br>corbishawelectricllc@brivanmail.com · www.corbishawelectric-example.com</div>
  </section>

  <section class="piece letter one">
    <div class="brand"><span class="dot"></span>Corbishaw Electric LLC</div>
    <div class="tiny body">Dear client, thank you for choosing us for your electrical<br>work.<br><br>We look forward to serving you.<br><br>Sincerely,</div>
    <div class="foot"></div>
  </section>

  <section class="piece letter two">
    <div class="brand"><span class="dot"></span>Corbishaw Electric LLC</div>
    <div class="tiny body">614 Linwood Avenue Jersey City, NJ 07305<br>1-855-48AMPRO<br>www.corbishawelectric-example.com</div>
    <div class="foot"></div>
  </section>

  <section class="piece note a"><div class="brand"><span class="dot"></span>Corbishaw Electric LLC</div><div class="tiny">1-855-48AMPRO</div></section>
  <section class="piece note b"><div class="brand"><span class="dot"></span>Corbishaw Electric LLC</div><div class="tiny">corbishawelectricllc@brivanmail.com</div></section>
  <section class="piece note c"><div class="brand light"><span class="dot"></span>Corbishaw Electric LLC</div><div class="tiny">TradeRankr · Zorvik · NestGauge</div></section>

  <section class="piece envelope">
    <svg width="120" height="58" viewBox="0 0 120 58" aria-hidden="true">
      <path d="M0 0 L60 30 L120 0 Z" fill="var(--navy)"/>
      <path d="M0 0 L60 24 L120 0" fill="none" stroke="var(--green)" stroke-width="2"/>
    </svg>
    <div class="brand"><span class="dot"></span>Corbishaw Electric</div>
  </section>
  <section class="piece envelope-back"><div class="brand"><span class="dot"></span>Corbishaw Electric LLC</div><div class="tiny">www.corbishawelectric-example.com</div></section>

  <section class="piece shirt s1"><div class="brand"><span class="dot"></span>Corbishaw Electric</div></section>
  <section class="piece shirt s2"><div class="brand"><span class="dot"></span>Corbishaw Electric</div><div class="tiny">1-855-48AMPRO</div></section>
  <section class="piece shirt navy s3"><div class="brand light"><span class="dot"></span>Corbishaw Electric</div></section>
  <section class="piece shirt navy s4"><div class="brand light"><span class="dot"></span>Corbishaw Electric</div><div class="tiny">1-855-48AMPRO</div></section>

  <section class="piece wrap w1"><div class="brand"><span class="dot"></span>Corbishaw Electric LLC</div><div class="tiny">RESIDENTIAL · COMMERCIAL · INDUSTRIAL</div><div class="band"><span>1-855-48AMPRO</span></div></section>
  <section class="piece wrap w2"><div class="brand"><span class="dot"></span>Corbishaw Electric LLC</div><div class="tiny">www.corbishawelectric-example.com</div><div class="band"><span>1-855-48AMPRO</span></div></section>
  <section class="piece wrap w3"><div class="brand"><span class="dot"></span>Corbishaw Electric LLC</div><div class="tiny">RESIDENTIAL · COMMERCIAL · INDUSTRIAL</div><div class="band"><span>www.corbishawelectric-example.com</span></div></section>
  <section class="piece wrap w4"><div class="brand"><span class="dot"></span>Corbishaw Electric LLC</div><div class="tiny">TradeRankr · Zorvik · NestGauge</div><div class="band"><span>1-855-48AMPRO</span></div></section>

</main>
</body>
</html>
```